PowerPoint Template Design for Management Consultancy

I need a PPT template for a new management consulting company. I want a modern look that uses dark blues and greys for divider slides, white content slides and a creative use of the logo in the slides. The supplied images are used on the website so I'd like to incorporate these into the theme

Target Market(s)

Management Consulting

Industry/Entity Type

Consulting

Font styles to use
Sans Serif

Colors
3277b5

Requirements
Must have
• Options for title slide, divider slides, content slides using the logo provided
Plain white content slides with creative use of logo
Color theme uses dark blues and greys
Nice to have
• Light and dark theme

```html
<!DOCTYPE html>
<html lang="en">
<head>
<meta charset="utf-8">
<title>Corvane Consulting – Presentation Template</title>
<link rel="stylesheet" href="https://fonts.googleapis.com/css2?family=Montserrat:wght@500;600&family=Source+Sans+3:wght@400;500&display=swap">
<style>
  :root {
    --navy: #00005a;
    --accent-stripe: #6b9cff;
    --brand-blue: #2f6cf0;
    --ink: #12129a;
    --outline: #1c1c8c;
    --paper: #ffffff;
    --photo-sky: #f8f1e6;
    --photo-haze: #9cc6d6;
    --photo-ridge: #5b7f9c;
    --photo-rock: #0b0b0b;
  }
  * { box-sizing: border-box; margin: 0; padding: 0; }
  html, body { width: 1200px; height: 1000px; overflow: hidden; background: var(--paper); }
  .canvas { position: relative; width: 1200px; height: 1000px; background: var(--paper); }

  /* Title slide */
  .title-slide { position: absolute; left: 0; top: 0; width: 1200px; height: 522px; background: var(--navy); overflow: hidden; }
  .title-slide__art { position: absolute; inset: 0; }
  .title-slide__heading {
    position: absolute; left: 51px; top: 52px;
    font-family: "Montserrat", sans-serif; font-weight: 500;
    font-size: 68px; letter-spacing: 4px; color: var(--paper); line-height: 1;
  }
  .title-slide__sub {
    position: absolute; left: 52px; top: 152px;
    font-family: "Source Sans 3", sans-serif; font-weight: 400;
    font-size: 56px; letter-spacing: 1px; color: var(--paper); line-height: 1;
  }
  .brand {
    font-family: "Montserrat", sans-serif; font-weight: 600;
    color: var(--brand-blue); text-align: center; line-height: 1;
  }
  .brand__name { display: block; }
  .brand__tag { display: block; }
  .title-slide__brand { position: absolute; left: 60px; top: 448px; width: 160px; }
  .title-slide__brand .brand__name { font-size: 34px; letter-spacing: 1px; }
  .title-slide__brand .brand__tag { font-size: 11px; letter-spacing: 2px; margin-top: 5px; }

  /* Content slide */
  .content-slide { position: absolute; left: 0; top: 522px; width: 1200px; height: 478px; }
  .content-slide__heading {
    position: absolute; left: 42px; top: 20px;
    font-family: "Source Sans 3", sans-serif; font-weight: 500;
    font-size: 35px; color: var(--ink); line-height: 1;
  }
  .agenda { position: absolute; list-style: none; top: 61px; }
  .agenda--left { left: 57px; }
  .agenda--right { left: 816px; }
  .agenda__item { position: relative; width: 337px; height: 46px; margin-bottom: 5.8px; }
  .agenda__item--shift { left: -3px; }
  .agenda__label {
    position: absolute; left: 46px; top: 3px; width: 291px; height: 39px;
    border: 1px solid var(--outline); border-radius: 0 6px 6px 0;
    display: flex; align-items: center; justify-content: center; padding-left: 16px;
    font-family: "Montserrat", sans-serif; font-weight: 500; font-size: 18px;
    letter-spacing: 0.8px; color: var(--ink); background: var(--paper);
  }
  .agenda__number {
    position: absolute; left: 0; top: 0; width: 64px; height: 46px;
    border: 1px solid var(--outline); border-radius: 50%; background: var(--paper);
    display: flex; align-items: center; justify-content: center;
    font-family: "Montserrat", sans-serif; font-weight: 500; font-size: 18px; color: var(--ink);
  }
  .content-slide__brand { position: absolute; left: 446px; top: 214px; width: 320px; }
  .content-slide__brand .brand__name { font-size: 56px; letter-spacing: 3px; }
  .content-slide__brand .brand__tag { font-size: 17px; letter-spacing: 4px; margin-top: 4px; }
</style>
</head>
<body>
<main class="canvas">
  <section class="title-slide">
    <svg class="title-slide__art" width="1200" height="522" viewBox="0 0 1200 522">
      <defs>
        <linearGradient id="scene-tones" x1="0" y1="0" x2="1" y2="1">
          <stop offset="0" stop-color="var(--photo-sky)"/>
          <stop offset="0.35" stop-color="var(--photo-haze)"/>
          <stop offset="0.55" stop-color="var(--photo-ridge)"/>
          <stop offset="0.72" stop-color="var(--photo-rock)"/>
          <stop offset="1" stop-color="var(--photo-rock)"/>
        </linearGradient>
      </defs>
      <polygon role="img" aria-label="Photo: two climbers silhouetted on a rocky ridge, one helping the other up, above misty blue mountains at dawn"
               points="600,0 1200,0 1200,514 935,514" fill="url(#scene-tones)"/>
      <polygon class="title-slide__stripe" points="586,0 600,0 935,514 918,514" fill="var(--accent-stripe)"/>
      <rect x="0" y="514" width="1200" height="8" fill="var(--navy)"/>
    </svg>
    <h1 class="title-slide__heading">Main Title</h1>
    <p class="title-slide__sub">Sub Information</p>
    <div class="brand title-slide__brand">
      <span class="brand__name">CORVANE</span>
      <span class="brand__tag">CONSULTING</span>
    </div>
  </section>

  <section class="content-slide">
    <h2 class="content-slide__heading">Content Slides</h2>
    <ol class="agenda agenda--left">
      <li class="agenda__item"><span class="agenda__label">Type Information</span><span class="agenda__number">#</span></li>
      <li class="agenda__item"><span class="agenda__label">Type Information</span><span class="agenda__number">#</span></li>
      <li class="agenda__item"><span class="agenda__label">Type Information</span><span class="agenda__number">#</span></li>
      <li class="agenda__item agenda__item--shift"><span class="agenda__label">Type Information</span><span class="agenda__number">#</span></li>
      <li class="agenda__item agenda__item--shift"><span class="agenda__label">Type Information</span><span class="agenda__number">#</span></li>
      <li class="agenda__item agenda__item--shift"><span class="agenda__label">Type Information</span><span class="agenda__number">#</span></li>
      <li class="agenda__item agenda__item--shift"><span class="agenda__label">Type Information</span><span class="agenda__number">#</span></li>
    </ol>
    <div class="brand content-slide__brand">
      <span class="brand__name">CORVANE</span>
      <span class="brand__tag">CONSULTING</span>
    </div>
    <ol class="agenda agenda--right">
      <li class="agenda__item"><span class="agenda__label">Type Information</span><span class="agenda__number">#</span></li>
      <li class="agenda__item"><span class="agenda__label">Type Information</span><span class="agenda__number">#</span></li>
      <li class="agenda__item"><span class="agenda__label">Type Information</span><span class="agenda__number">#</span></li>
      <li class="agenda__item agenda__item--shift"><span class="agenda__label">Type Information</span><span class="agenda__number">#</span></li>
      <li class="agenda__item agenda__item--shift"><span class="agenda__label">Type Information</span><span class="agenda__number">#</span></li>
      <li class="agenda__item agenda__item--shift"><span class="agenda__label">Type Information</span><span class="agenda__number">#</span></li>
      <li class="agenda__item agenda__item--shift"><span class="agenda__label">Type Information</span><span class="agenda__number">#</span></li>
    </ol>
  </section>
</main>
</body>
</html>
```